New Phone Case requires logo and packaging

We need a nice and sleek logo designed along with packaging for our Premium Phone Case brand

Our Brand Name is Vaxel
Please note this has nothing to do with a Rhino so don't put a Rhino in the logo
I've also attached a file called VAXEL Logo Inspiration, which shows something along the lines of the type of text we want to use. Please note i have photoshopped that image together from another logo we had, and i liked the text, but its for you to see what direction we want to go in. Also note i have shown different variations in that image file, use your imagination with it and show us a nice and clean logo.

We would like the Brand in upper caps such as VAXEL
The brand is for Premium Phone Cases. The first thing that should come to someones mind when looking at the branding is High Quality, Premium and Modern.

The look must be high end and modern

The design must portray high quality and premium!

Also i will say "Less is More". Don't cramp many things on the packaging and logo. We just want a nice, clean cut high quality logo and packaging

I have attached images of an example packaging from a few competitors. One is a standard open from top packaging, while another is a slide out packaging. Our packaging dimensions should be the same which are Packaging dimensions
Length = 18cm
Height = 1.5cm
Depth = 9.5cm

Also note the example packaging has a transparent front section to show which case is inside, this is optional if you want to have it. If not you can cover it all up.

Font styles to use
Other font styles liked:
• Any nice font but just not the standard everyday stuff like Arial, San Serif etc as i want it to be differentiated. A Font that shows Serious Quality and one that stands out would be awesome!

Colors

Designer to choose colors to be used in the design.

Requirements
Must have
• Must be a nice and clean design
• Packaging dimensions
• Length = 18cm
• Height = 1.5cm
• Depth = 9.5cm

```html
<!DOCTYPE html>
<html lang="en">
<head>
<meta charset="utf-8">
<title>Vaxel – Logo and Packaging Proposal</title>
<link rel="stylesheet" href="https://fonts.googleapis.com/css2?family=Barlow:wght@500&family=Barlow+Condensed:wght@400&family=Lato:wght@300&display=swap">
<style>
  :root {
    --page: #ffffff;
    --box: #2e2d32;
    --ink-light: #ffffff;
    --fold-line: #d9d9dc;
    --rule: #7a7a7a;
    --caption: #3a3a3a;
  }
  html, body {
    margin: 0;
    padding: 0;
    background: var(--page);
    overflow: hidden;
  }
  .sheet {
    width: 1200px;
    height: 848px;
    display: block;
    overflow: hidden;
  }
  .box-face { fill: var(--box); }
  .fold { stroke: var(--fold-line); stroke-width: 1; fill: none; }
  .window { fill: var(--page); }
  .wordmark {
    font-family: "Barlow", sans-serif;
    font-weight: 500;
    fill: var(--ink-light);
    letter-spacing: 1px;
  }
  .tagline {
    font-family: "Barlow Condensed", sans-serif;
    font-weight: 400;
    fill: var(--ink-light);
  }
  .footer-rule { stroke: var(--rule); stroke-width: 1; }
  .proposal-caption {
    font-family: "Lato", sans-serif;
    font-weight: 300;
    fill: var(--caption);
    font-size: 16px;
    letter-spacing: 7px;
  }
</style>
</head>
<body>
<svg class="sheet" viewBox="0 0 1200 848" xmlns="http://www.w3.org/2000/svg">
  <!-- packaging dieline -->
  <g class="dieline">
    <rect class="box-face" x="116" y="148" width="968" height="441"/>
    <rect class="window" x="280" y="186" width="640" height="184" rx="26" ry="26"/>
    <line class="fold" x1="176" y1="148" x2="176" y2="589"/>
    <line class="fold" x1="236" y1="148" x2="236" y2="589"/>
    <line class="fold" x1="964" y1="148" x2="964" y2="589"/>
    <line class="fold" x1="1024" y1="148" x2="1024" y2="589"/>
    <line class="fold" x1="116" y1="529" x2="1084" y2="529"/>
  </g>

  <!-- left side panel -->
  <g class="side-panel-left">
    <text class="wordmark" font-size="50" transform="translate(180,154) rotate(90)">VAXEL</text>
    <text class="tagline" font-size="15" transform="translate(184,400) rotate(90)">Premium Phone Case</text>
  </g>

  <!-- front face -->
  <g class="front-face">
    <text class="wordmark" font-size="80" x="240" y="518">VAXEL</text>
  </g>

  <!-- bottom flap -->
  <g class="bottom-flap">
    <text class="wordmark" font-size="46" x="240" y="583">VAXEL</text>
    <text class="tagline" font-size="15" x="956" y="584" text-anchor="end">Premium Phone Case</text>
  </g>

  <!-- right side panel -->
  <g class="side-panel-right">
    <text class="tagline" font-size="15" transform="translate(1020,277) rotate(-90)">Premium Phone Case</text>
    <text class="wordmark" font-size="46" transform="translate(1019,524) rotate(-90)">VAXEL</text>
  </g>

  <!-- presentation footer -->
  <g class="presentation-footer">
    <line class="footer-rule" x1="0" y1="742" x2="1200" y2="742"/>
    <text class="proposal-caption" x="1176" y="780" text-anchor="end">PROPOSAL FOR</text>
    <text class="proposal-caption" x="1176" y="801" text-anchor="end">VAXEL</text>
    <text class="proposal-caption" x="1176" y="822" text-anchor="end">LOGO AND PACKAGING</text>
  </g>
</svg>
</body>
</html>
```